Harbor Light Chapel: Steadfast Conference

We need a flyer, powerpoint, and possible email template for our Church's Bible Conference for October 6th-8th. The conference is called Steadfast (Holding Firmly to Scripture).

The purpose of the conference is that we would like to encourage believers to stand courageously on the absolute authority of God’s word, to know the truth and to stand courageously for it.

This is the Conference information below

Sunday: 9:30AM: Pastor Tobias Felderline: Delivered from Fear
11am: Dr. Martin Holloway: Standing for Righteousness in a politically correct society

7pm: Dr. Everett Prynne: Courageously facing Immortality

Monday: Dr. Martin Holloway: The Stand for Righteousness as a Christian Educator

Tuesday: Pastor Tobias Felderline: Courageously Proclaiming Christ in Muslim Territory

Wednesday: Dr. Everett Prynne: Stand for Righteousness in the Last Days

An idea that we had could be 3 or 4 people facing a large crowd, illuminated with the bible as their guide. I don't know how hard that would be to design, but basically something that emphasizes Steadfast in regards to the bible.

If you have any questions please message me at anytime, a team of 3 of us will be selecting the top design.
Updates

Project Deadline Extended
Reason: Some of our team members who are selecting had to travel abroad and won't be back in the office till monday. We also would like to see more designs as well.

Target Market(s)

All Ages

Industry/Entity Type

Church

Requirements
Must have
• Email
Flyer
Powerpoint describing Flyer: Could be two or 3 slides
Harbor Light Chapel
2013 Scripture Gathering

```html
<!DOCTYPE html>
<html lang="en">
<head>
<meta charset="utf-8">
<title>Steadfast Conference – Harbor Light Chapel</title>
<link href="https://fonts.googleapis.com/css2?family=League+Gothic&family=Oswald:wght@300;400;500;600;700&display=swap" rel="stylesheet">
<style>
  :root {
    --cream: #f6efdf;
    --ray-tan: #dcc49a;
    --gold: #c9a04a;
    --cross-gold: #c8962e;
    --title-red: #d4222b;
    --ink-gray: #6a6b6d;
    --band-dark: #333334;
    --day-gray: #b9b9b9;
    --text-light: #f2f2f2;
    --edge-tan: #a98a55;
  }
  * { margin: 0; padding: 0; box-sizing: border-box; }
  html, body { width: 927px; height: 1200px; overflow: hidden; background: #ffffff; }
  .flyer {
    position: relative;
    width: 927px;
    height: 1200px;
    overflow: hidden;
    font-family: "Oswald", "Arial Narrow", sans-serif;
    background:
      radial-gradient(circle at 500px 290px, #ffffff 0, var(--cream) 240px, var(--ray-tan) 620px, #c9ad7c 900px);
  }
  .backdrop { position: absolute; inset: 0; }
  .scene-art {
    position: absolute;
    left: 45px; top: 242px;
    width: 850px; height: 531px;
    background: linear-gradient(170deg, rgba(200,198,192,0.55) 0%, rgba(150,150,150,0.7) 40%, rgba(40,40,40,0.9) 100%);
    border-radius: 6px;
  }
  .header-line {
    position: absolute;
    left: 79px; top: 12px;
    width: 770px;
    font-size: 25.5px;
    font-weight: 600;
    color: var(--ink-gray);
    letter-spacing: 0.3px;
    white-space: nowrap;
  }
  .title-row {
    position: absolute;
    left: 76px; top: 36px;
    width: 776px;
    display: flex;
    align-items: flex-start;
    justify-content: space-between;
  }
  .event-title {
    font-size: 118px;
    line-height: 1;
    font-weight: 600;
    color: var(--title-red);
    letter-spacing: -1px;
  }
  .cross-mark { width: 48px; height: 116px; margin-top: 14px; }
  .tagline {
    font-weight: 600;
    color: var(--ink-gray);
    text-align: center;
    line-height: 0.98;
    margin-top: 6px;
  }
  .tagline .big { display: block; font-size: 44px; }
  .tagline .small { display: block; font-size: 31px; }
  .event-date {
    position: absolute;
    left: 79px; top: 160px;
    font-size: 62px;
    font-weight: 500;
    color: var(--ink-gray);
    line-height: 1;
  }
  .schedule {
    position: absolute;
    left: 79px; top: 790px;
    width: 830px;
    color: var(--text-light);
  }
  .schedule-heading {
    font-size: 62px;
    font-weight: 500;
    line-height: 1;
    margin-bottom: 22px;
  }
  .day-row {
    display: flex;
    align-items: center;
  }
  .day-row + .day-row { margin-top: 24px; }
  .day-name {
    font-family: "League Gothic", "Oswald", sans-serif;
    font-size: 50px;
    color: var(--day-gray);
    line-height: 1;
    width: 71px;
    flex-shrink: 0;
    white-space: nowrap;
  }
  .sessions { font-size: 16.5px; line-height: 1.15; white-space: nowrap; }
  .session { display: flex; align-items: baseline; }
  .time { width: 54px; flex-shrink: 0; font-weight: 400; }
  .divider { margin: 0 7px 0 2px; }
  .speaker { color: var(--gold); font-weight: 600; text-transform: uppercase; margin-right: 6px; }
  .topic { font-weight: 300; }
</style>
</head>
<body>
<div class="flyer">
  <svg class="backdrop" width="927" height="1200" viewBox="0 0 927 1200" aria-hidden="true">
    <defs>
      <linearGradient id="edgeLeft" x1="0" x2="1">
        <stop offset="0" stop-color="#a98a55" stop-opacity="0.85"/>
        <stop offset="1" stop-color="#a98a55" stop-opacity="0"/>
      </linearGradient>
      <linearGradient id="edgeRight" x1="1" x2="0">
        <stop offset="0" stop-color="#a98a55" stop-opacity="0.85"/>
        <stop offset="1" stop-color="#a98a55" stop-opacity="0"/>
      </linearGradient>
    </defs>
    <rect x="0" y="0" width="30" height="1200" fill="url(#edgeLeft)"/>
    <rect x="897" y="0" width="30" height="1200" fill="url(#edgeRight)"/>
  </svg>

  <div class="scene-art" role="img" aria-label="Silhouettes of three people reaching toward an open Bible, facing a large cheering crowd, lit by rays of light"></div>

  <svg class="backdrop" width="927" height="1200" viewBox="0 0 927 1200" aria-hidden="true">
    <polygon points="0,598 927,894 927,1200 0,1200" fill="var(--band-dark)"/>
  </svg>

  <header>
    <p class="header-line">HARBOR LIGHT CHAPEL PRESENTS ITS 2013 SCRIPTURE GATHERING</p>
    <div class="title-row">
      <h1 class="event-title">STEADFAST</h1>
      <svg class="cross-mark" viewBox="0 0 48 116" aria-hidden="true">
        <rect x="18" y="0" width="12" height="116" fill="var(--cross-gold)"/>
        <rect x="0" y="26" width="48" height="12" fill="var(--cross-gold)"/>
      </svg>
      <p class="tagline"><span class="big">HOLDING</span><span class="small">FIRMLY TO</span><span class="big">SCRIPTURE</span></p>
    </div>
    <p class="event-date">OCTOBER 6-8, 2013</p>
  </header>

  <section class="schedule">
    <h2 class="schedule-heading">SCHEDULE:</h2>

    <div class="day-row sun">
      <div class="day-name">SUN</div>
      <div class="sessions">
        <div class="session"><span class="time">9:30am</span><span class="divider">|</span><span class="speaker">Pastor Tobias Felderline</span><span class="topic">/ delivered from fear</span></div>
        <div class="session"><span class="time">11am</span><span class="divider">|</span><span class="speaker">Dr. Martin Holloway</span><span class="topic">/ standing for righteousness in a politically correct society</span></div>
        <div class="session"><span class="time">7pm</span><span class="divider">|</span><span class="speaker">Dr. Everett Prynne</span><span class="topic">/ courageously facing immortality</span></div>
      </div>
    </div>

    <div class="day-row mon">
      <div class="day-name">MON</div>
      <div class="sessions">
        <div class="session"><span class="time">7:30pm</span><span class="divider">|</span><span class="speaker">Dr. Martin Holloway</span><span class="topic">/ the stand for righteousness as a christian educator</span></div>
      </div>
    </div>

    <div class="day-row tues">
      <div class="day-name">TUES</div>
      <div class="sessions">
        <div class="session"><span class="time">7:30pm</span><span class="divider">|</span><span class="speaker">Pastor Tobias Felderline</span><span class="topic">/ courageously proclaiming christ in muslim territory</span></div>
      </div>
    </div>

    <div class="day-row wed">
      <div class="day-name">WED</div>
      <div class="sessions">
        <div class="session"><span class="time">7:30pm</span><span class="divider">|</span><span class="speaker">Dr. Everett Prynne</span><span class="topic">/ stand for righteousness in the last days</span></div>
      </div>
    </div>
  </section>
</div>
</body>
</html>
```